Placing my newer logo on my existing business card

I have a business card that I had you guys do years ago, then I changed my logo, I love both my business card and my logo. The challenge is both my logo and my business card are very similar in color. So I'm not sure how to make my logo stand out.

Sick

```html
<!DOCTYPE html>
<html lang="en">
<head>
<meta charset="utf-8">
<title>Aspen Vitality Wellness Clinic – Business Card</title>
<link href="https://fonts.googleapis.com/css2?family=Cinzel:wght@500;600&family=Lato:wght@400;700&family=Great+Vibes&display=swap" rel="stylesheet">
<style>
  :root {
    --stage: #3a3a3a;
    --paper: #ffffff;
    --navy: #2e3f4b;
    --navy-soft: #364956;
    --rust: #b4472a;
    --mist: #8fa9b0;
    --ink-light: #e6ecee;
  }
  * { box-sizing: border-box; margin: 0; padding: 0; }
  html, body { width: 1200px; height: 875px; overflow: hidden; }
  body {
    background: var(--stage);
    display: flex; align-items: center; justify-content: center; gap: 40px;
    font-family: "Lato", sans-serif;
  }
  .card {
    position: relative; width: 540px; height: 315px; border-radius: 22px; overflow: hidden;
  }
  /* Front */
  .card--front { background: var(--paper); }
  .brand {
    position: absolute; left: 0; right: 0; top: 40px;
    display: flex; flex-direction: column; align-items: center; gap: 10px;
  }
  .brand__dot { width: 46px; height: 46px; border-radius: 50%; background: var(--mist); }
  .brand__name {
    font-family: "Cinzel", serif; font-weight: 600; color: var(--rust);
    font-size: 22px; line-height: 1.1; text-align: center; letter-spacing: 1.5px;
  }
  .appointment { position: absolute; left: 44px; right: 44px; top: 178px; }
  .field-row { display: flex; align-items: flex-end; gap: 6px; margin-bottom: 22px; }
  .field-label {
    font-size: 11px; letter-spacing: 1px; color: var(--rust); text-transform: uppercase;
  }
  .field-line { flex: 1; border-bottom: 1px dotted var(--rust); height: 1px; margin-bottom: 3px; }
  .tagline {
    position: absolute; right: 48px; bottom: 26px;
    font-family: "Great Vibes", cursive; font-size: 34px; color: var(--rust);
  }
  /* Back */
  .card--back { background: var(--navy); color: var(--ink-light); }
  .watermark {
    position: absolute; left: -60px; top: 60px; width: 300px; height: 300px;
    border-radius: 50%; background: var(--navy-soft);
  }
  .back-brand {
    position: absolute; right: 36px; top: 30px; width: 230px;
    display: flex; flex-direction: column; align-items: center; gap: 8px;
  }
  .back-brand .brand__dot { width: 38px; height: 38px; }
  .back-brand .brand__name { font-size: 16px; }
  .divider {
    position: absolute; left: 36px; right: 36px; top: 160px; height: 1px; background: var(--rust);
  }
  .person { position: absolute; left: 36px; top: 100px; }
  .person__name {
    font-family: "Cinzel", serif; font-weight: 600; color: var(--rust);
    font-size: 24px; letter-spacing: 1px;
  }
  .person__role { font-size: 14px; color: var(--mist); margin-top: 2px; }
  .contacts { position: absolute; left: 36px; top: 182px; list-style: none; }
  .contacts li {
    display: flex; align-items: center; gap: 10px; font-size: 13px; margin-bottom: 9px;
  }
  .contacts svg { width: 13px; height: 13px; fill: var(--rust); flex-shrink: 0; }
  .address {
    position: absolute; right: 36px; top: 182px; text-align: right;
    font-size: 13px; line-height: 1.55; font-style: normal;
  }
</style>
</head>
<body>

  <section class="card card--front" aria-label="Appointment card, front">
    <div class="brand">
      <span class="brand__dot"></span>
      <p class="brand__name">Aspen Vitality<br>Wellness Clinic</p>
    </div>
    <div class="appointment">
      <div class="field-row">
        <span class="field-label">Name</span><span class="field-line"></span>
      </div>
      <div class="field-row">
        <span class="field-label">Date</span><span class="field-line"></span>
        <span class="field-label">Time</span><span class="field-line"></span>
        <span class="field-label">AM\PM</span>
      </div>
    </div>
    <p class="tagline">Let's Make it Happen</p>
  </section>

  <section class="card card--back" aria-label="Business card, back">
    <div class="watermark" role="img" aria-label="Faint large brand emblem area"></div>
    <div class="back-brand">
      <span class="brand__dot"></span>
      <p class="brand__name">Aspen Vitality<br>Wellness Clinic</p>
    </div>
    <div class="person">
      <p class="person__name">Marla Whitfield</p>
      <p class="person__role">Director</p>
    </div>
    <div class="divider"></div>
    <ul class="contacts">
      <li><svg viewBox="0 0 24 24"><path d="M6.6 10.8a15 15 0 0 0 6.6 6.6l2.2-2.2c.3-.3.7-.4 1-.2 1.1.4 2.3.6 3.6.6.6 0 1 .4 1 1V20c0 .6-.4 1-1 1A17 17 0 0 1 3 4c0-.6.4-1 1-1h3.5c.6 0 1 .4 1 1 0 1.3.2 2.5.6 3.6.1.3 0 .7-.2 1z"/></svg>(555)014-2210</li>
      <li><svg viewBox="0 0 24 24"><path d="M6 3h12v5H6zM4 9h16a2 2 0 0 1 2 2v6h-4v4H6v-4H2v-6a2 2 0 0 1 2-2zm4 7v3h8v-3z"/></svg>(555)014-2211</li>
      <li><svg viewBox="0 0 24 24"><path d="M2 5h20v14H2zm2 2v.5l8 5 8-5V7l-8 5z"/></svg>hello@aspenvitalityclinic.com</li>
      <li><svg viewBox="0 0 24 24"><path d="M12 2a10 10 0 1 0 0 20 10 10 0 0 0 0-20zm0 2c1 1.3 1.8 3 2.1 5H9.9C10.2 7 11 5.3 12 4zM4.3 11h3.6a14 14 0 0 0 0 2H4.3a8 8 0 0 1 0-2zm5.6 0h4.2a12 12 0 0 1 0 2H9.9a12 12 0 0 1 0-2zm6.2 0h3.6a8 8 0 0 1 0 2h-3.6a14 14 0 0 0 0-2zM9.9 15h4.2c-.3 2-1.1 3.7-2.1 5-1-1.3-1.8-3-2.1-5z"/></svg>aspenvitalityclinic.com</li>
    </ul>
    <address class="address">
      Aspen Vitality Wellness<br>
      Clinic &amp; Therapy<br>
      1847 Larch Street Ste#2<br>
      Millbrook, UT 84000
    </address>
  </section>

</body>
</html>
```